Bold Website Design for Fitness Trainer - No Coding

We are in need of a bold and unique website design for a personal fitness training company, www.TessaLorvel.com. We need DESIGN ONLY for three pages. These will be a homepage, a lead capture page, and one internal page with a sidebar. The design will be used for coding a wordpress theme, if that matters for the designer.

Tessa Lorvel Fitness Training
2738 E 19th St #415
Austin, TX 78705
512-607-4918
http://www.tessalorvel.com

Target Market(s)

18-45 year old male and females making 80k+ a year and looking to get stronger and in shape.

Industry/Entity Type

Fitness

Number of Pages Required

3 page

Font styles to use
Sans Serif

Requirements
Must have
• See attached design specs file.
Nice to have
Should not have
• Boxed layout.
• Dark Background.

```html
<!DOCTYPE html>
<html lang="en">
<head>
<meta charset="utf-8">
<title>Tessa Lorvel Fitness Training</title>
<link href="https://fonts.googleapis.com/css2?family=Open+Sans:wght@400;600;700;800&display=swap" rel="stylesheet">
<style>
  :root{
    --yellow:#f4c300;
    --dark:#1d1d1d;
    --darker:#141414;
    --blue:#1c98d6;
    --red:#d3202a;
    --band:#d6d6d6;
    --text:#333333;
    --muted:#6b6b6b;
    --white:#ffffff;
    --ring:#e4e4e4;
  }
  *{box-sizing:border-box;margin:0;padding:0}
  html,body{width:1200px;height:2288px;overflow:hidden}
  body{font-family:"Open Sans",Arial,sans-serif;color:var(--text);background:var(--white)}
  .page{width:1200px;height:2288px;position:relative}

  .site-header{height:148px;display:flex;align-items:center;justify-content:center;gap:18px}
  .brand-mark{width:96px;height:96px;border-radius:50%;background:var(--yellow)}
  .brand-text{display:flex;flex-direction:column}
  .brand-name{font-size:52px;font-weight:800;color:var(--dark);line-height:1}
  .brand-tag{font-size:15px;font-weight:600;color:var(--dark);letter-spacing:2px;margin-top:6px}

  .main-nav{height:44px;background:var(--yellow);display:flex;justify-content:center;align-items:center;gap:44px}
  .main-nav a{color:var(--white);font-weight:700;font-size:17px;text-decoration:none}

  .hero-photo{height:468px;background:linear-gradient(180deg,#dadada 0%,#c2c2c2 70%,#a9a9a9 100%)}
  .hero-bar{height:120px;background:var(--dark);display:flex;align-items:center;justify-content:center;gap:60px}
  .hero-bar p{color:var(--white);font-size:18px}
  .btn-enquire{background:var(--red);color:var(--white);font-size:15px;font-weight:600;padding:8px 44px;border-radius:20px}

  .services{height:500px;padding-top:56px;text-align:center}
  .section-title{font-size:40px;font-weight:700;color:var(--blue);line-height:1.2}
  .section-sub{font-size:22px;font-weight:600;color:var(--dark);margin-top:2px}
  .section-copy{width:560px;margin:14px auto 0;font-size:14px;line-height:1.55;color:var(--muted)}
  .service-row{display:flex;justify-content:center;gap:70px;margin-top:50px}
  .service-photo{width:180px;height:180px;border-radius:50%;background:radial-gradient(circle at 40% 35%,#8a8a94,#5d5d68);border:3px solid #444}

  .testimonials{height:280px;background:var(--band);text-align:center;padding-top:36px}
  .testimonials .section-title{color:var(--dark)}
  .quote-row{display:flex;justify-content:center;gap:80px;margin-top:22px}
  .quote{width:340px}
  .quote h3{font-size:20px;font-weight:600;color:var(--dark)}
  .quote p{font-size:14px;line-height:1.55;color:var(--muted);margin-top:8px;text-align:left}

  .feature{height:520px;text-align:center;padding-top:58px}
  .feature-title{font-size:27px;font-weight:600;color:var(--dark);letter-spacing:.5px;line-height:1.3}
  .feature-title strong{font-weight:800}
  .blog-row{display:flex;justify-content:center;gap:170px;margin-top:26px}
  .blog-card{width:260px}
  .blog-thumb{width:150px;height:150px;border-radius:50%;background:var(--yellow);border:9px solid var(--ring);margin:0 auto}
  .blog-card h4{font-size:17px;font-weight:700;color:var(--dark);margin-top:8px;line-height:1.3}
  .blog-card .label{display:block;font-size:12px;color:var(--muted)}
  .blog-card p{font-size:13px;line-height:1.5;color:var(--muted);margin-top:10px}

  .site-footer{position:absolute;left:0;top:2080px;width:1200px;height:208px;background:var(--darker);color:var(--white)}
  .footer-cols{display:flex;justify-content:center;padding-top:36px}
  .footer-col{padding:0 34px}
  .footer-col + .footer-col{border-left:1px solid #444}
  .footer-col h5{font-size:17px;font-weight:600;letter-spacing:1px}
  .social{display:flex;gap:10px;margin-top:14px}
  .social span{width:28px;height:28px;background:#3f3f3f;display:block}
  .signup-input{margin-top:14px;width:240px;height:26px;background:#3a3a3a;color:#999;font-size:12px;padding:4px 10px}
  .contact{display:flex;gap:40px;margin-top:10px;font-size:12px;line-height:1.6;color:#bbb}
  .copyright{position:absolute;bottom:24px;width:100%;text-align:center;font-size:12px;color:#888}
</style>
</head>
<body>
<div class="page">
  <header class="site-header">
    <div class="brand-mark"></div>
    <div class="brand-text">
      <span class="brand-name">Tessa Lorvel</span>
      <span class="brand-tag">FITNESS TRAINING</span>
    </div>
  </header>
  <nav class="main-nav">
    <a href="#">HOME</a><a href="#">Link1</a><a href="#">Link2</a><a href="#">CONTACT</a>
  </nav>

  <div class="hero-photo" role="img" aria-label="Photo of a fitness trainer flexing against a light grey wall"></div>
  <div class="hero-bar">
    <p>Lorem ipsum dolor sit amet, consectetur adipiscing elit.</p>
    <span class="btn-enquire">Enquire</span>
  </div>

  <section class="services">
    <h2 class="section-title">SERVICES</h2>
    <p class="section-sub">Lorem Ipsum Dolor Sit Amet</p>
    <p class="section-copy">Lorem ipsum dolor sit amet, consectetur adipiscing elit. Aenean commodo ligula eget dolor. Aenean massa. Cum sociis natoque penatibus et magnis dis parturient montes, nascetur ridiculus mus.</p>
    <div class="service-row">
      <div class="service-photo" role="img" aria-label="Service photo"></div>
      <div class="service-photo" role="img" aria-label="Service photo"></div>
      <div class="service-photo" role="img" aria-label="Service photo"></div>
    </div>
  </section>

  <section class="testimonials">
    <h2 class="section-title">TESTIMONIALS</h2>
    <div class="quote-row">
      <div class="quote">
        <h3>Lorem Ipsum Dolor Sit Amet</h3>
        <p>Lorem ipsum dolor sit amet, consectetur adipiscing elit. Aenean commodo ligula eget dolor. Aenean massa. Cum sociis natoque penatibus et magnis dis parturient montes, nascetur ridiculus mus.</p>
      </div>
      <div class="quote">
        <h3>Lorem Ipsum Dolor Sit Amet</h3>
        <p>Lorem ipsum dolor sit amet, consectetur adipiscing elit. Aenean commodo ligula eget dolor. Aenean massa. Cum sociis natoque penatibus et magnis dis parturient montes, nascetur ridiculus mus.</p>
      </div>
    </div>
  </section>

  <section class="feature">
    <h2 class="feature-title">LOREM IPSUM DOLOR SIT AMET, CONSECTETUR <strong>ADIPISCING ELIT.</strong></h2>
    <p class="section-copy">Lorem ipsum dolor sit amet, consectetur adipiscing elit. Aenean commodo ligula eget dolor. Aenean massa. Cum sociis natoque penatibus et magnis dis parturient montes, nascetur ridiculus mus.</p>
    <div class="blog-row">
      <div class="blog-card">
        <div class="blog-thumb" role="img" aria-label="Blog post image"></div>
        <h4>Blog</h4>
        <span class="label">Lorem ipsum</span>
        <p>Lorem ipsum dolor sit amet, consectetur adipiscing elit. Aenean commodo ligula.</p>
      </div>
      <div class="blog-card">
        <div class="blog-thumb" role="img" aria-label="Blog post image"></div>
        <h4>Blog</h4>
        <span class="label">Lorem ipsum</span>
        <p>Lorem ipsum dolor sit amet, consectetur adipiscing elit. Aenean commodo ligula.</p>
      </div>
    </div>
  </section>

  <footer class="site-footer">
    <div class="footer-cols">
      <div class="footer-col">
        <h5>CONNECT</h5>
        <div class="social"><span></span><span></span><span></span></div>
      </div>
      <div class="footer-col">
        <h5>SIGN UP AND RECEIVE UPDATES!</h5>
        <div class="signup-input">Enter email</div>
      </div>
      <div class="footer-col">
        <h5>CONTACT US</h5>
        <div class="contact">
          <div>2738 E 19th St #415<br>Austin, TX 78705</div>
          <div>512-607-4918<br>www.TessaLorvel.com</div>
        </div>
      </div>
    </div>
    <p class="copyright">© All rights reserved.</p>
  </footer>
</div>
</body>
</html>
```